" E-commerce voltado para vendas moda em geral, roupas masculinas e femininas, acessorios unissex, relogios, sapatos, oculos, casual e contemporanea, nacionais e importadas, artigos de luxo e multimarcas. "

```html
<!DOCTYPE html>
<html lang="pt-BR">
<head>
<meta charset="utf-8">
<title>VESTA77 Multimarcas – Pasta</title>
<link href="https://fonts.googleapis.com/css2?family=Oswald:wght@400;700&family=Roboto:wght@400&display=swap" rel="stylesheet">
<style>
  :root {
    --page: #ffffff;
    --red-light: #c4161c;
    --red-dark: #8e0a0f;
    --gold: #d9a441;
    --ink-soft: #7a7a7a;
    --ghost: #f3e3e3;
  }
  * { margin: 0; padding: 0; box-sizing: border-box; }
  html, body {
    width: 1200px; height: 1200px; overflow: hidden;
    background: var(--page);
  }
  .canvas { position: relative; width: 1200px; height: 1200px; }

  .folder { position: absolute; left: 240px; top: 197px; width: 725px; height: 631px; }

  .panel-inside {
    position: absolute; left: 12px; top: 0; width: 355px; height: 506px;
    background: var(--page);
    box-shadow: 0 0 0 1px #ececec;
  }
  .crest-decoration {
    position: absolute; left: 30px; top: 20px; width: 250px; height: 420px;
    background: radial-gradient(ellipse at 45% 40%, var(--ghost) 0%, rgba(243,227,227,0.5) 55%, rgba(255,255,255,0) 80%);
  }
  .inside-brand {
    position: absolute; left: 0; width: 355px; top: 432px; text-align: center;
  }
  .inside-brand .name {
    font-family: "Oswald", sans-serif; font-weight: 700; font-size: 20px;
    color: var(--red-light); letter-spacing: 1px;
  }
  .contact {
    margin-top: 8px; font-family: "Roboto", sans-serif; font-size: 8px;
    line-height: 11px; color: var(--ink-soft);
  }

  .panel-cover {
    position: absolute; left: 367px; top: 0; width: 358px; height: 506px;
    background: linear-gradient(135deg, var(--red-light) 0%, #a80f15 55%, var(--red-dark) 100%);
  }
  .cover-brand {
    position: absolute; left: 0; width: 358px; top: 222px; text-align: center; color: #fff;
  }
  .cover-brand .name {
    font-family: "Oswald", sans-serif; font-weight: 700; font-size: 40px;
    letter-spacing: 2px; line-height: 1;
  }
  .cover-brand .tagline {
    font-family: "Oswald", sans-serif; font-weight: 400; font-size: 9px;
    letter-spacing: 4px; margin-top: 4px;
  }
  .cover-rule {
    position: absolute; left: 29px; right: 5px; top: 288px; height: 3px;
    background: var(--gold);
  }

  .pocket { position: absolute; left: 0; top: 506px; width: 367px; height: 125px; }
</style>
</head>
<body>
<div class="canvas">
  <div class="folder">
    <section class="panel-inside">
      <div class="crest-decoration" role="img" aria-label="Faint heraldic lion crest watermark"></div>
      <div class="inside-brand">
        <div class="name">VESTA77</div>
        <div class="contact">
          <div>(11) 5555-0199</div>
          <div>Rua das Flores, 120</div>
          <div>contato@vesta77.com</div>
        </div>
      </div>
    </section>

    <section class="panel-cover">
      <div class="cover-brand">
        <div class="name">VESTA77</div>
        <div class="tagline">MULTIMARCAS</div>
      </div>
      <div class="cover-rule"></div>
    </section>

    <svg class="pocket" viewBox="0 0 367 125" aria-hidden="true">
      <defs>
        <linearGradient id="pocketFill" x1="0" y1="0" x2="1" y2="1">
          <stop offset="0" stop-color="#c4161c"/>
          <stop offset="1" stop-color="#8e0a0f"/>
        </linearGradient>
      </defs>
      <path d="M12 0 H367 V125 H12 Z" fill="url(#pocketFill)"/>
      <path d="M0 26 C40 18 60 22 70 50 C78 78 68 110 64 125 H0 Z" fill="#ffffff"/>
      <path d="M0 26 C40 18 60 22 70 50 C78 78 68 110 64 125" fill="none" stroke="#e6e6e6" stroke-width="1"/>
    </svg>
  </div>
</div>
</body>
</html>
```